Life Coach for Lawyers Business Card Design

Elegant, original, business card design for life coaching service for associate attorneys who work in big law and struggle with stress, overwhelm, and time management. Double sided design.

Target Market(s)

Women associate attorneys who work in big law and struggle with stress, overwhelm, and time management.

Industry/Entity Type

Life Coaching

Contact Information for Business Card

Marissa Pendrell
Life Coach
518.677.3941
calmbriefcounsel.net
marissa@calmbriefcounsel.net
@calmbriefcounsel (Instagram)

Font styles to use
Other font styles liked:
• Silver South font duo. See uploaded files.

Requirements
Must have
• Icons for phone, website, email, and Instagram instead of words. Specific colors used in my logo (171B2B, 421121, FFFFFF)
Nice to have
• Foil. Embossed. Feminine design.
Should not have
• Any colors other than those used in logo. See uploaded files.

```html
<!DOCTYPE html>
<html lang="en">
<head>
<meta charset="utf-8">
<title>Calm Brief Counsel — Business Card</title>
<link rel="stylesheet" href="https://fonts.googleapis.com/css2?family=Playfair+Display:wght@400;700&family=Libre+Baskerville&display=swap">
<style>
  :root {
    --navy: #171B2B;
    --wine: #421121;
    --white: #FFFFFF;
    --paper: #EEEDEA;
    --backdrop: #26272B;
  }
  html, body {
    margin: 0;
    padding: 0;
    width: 1200px;
    height: 900px;
    overflow: hidden;
    background: var(--backdrop);
  }
  .canvas {
    position: relative;
    width: 1200px;
    height: 900px;
  }
  .card {
    position: absolute;
    width: 520px;
    height: 297px;
    background: var(--paper);
    border-radius: 3px;
    overflow: hidden;
    box-shadow: 0 14px 30px rgba(0,0,0,0.45);
  }
  .card--front { left: 90px; top: 170px; }
  .card--back { left: 590px; top: 430px; }

  .front-wordmark {
    position: absolute;
    inset: 0;
    display: flex;
    align-items: center;
    justify-content: center;
    font-family: "Playfair Display", Georgia, serif;
    font-weight: 400;
    font-size: 38px;
    letter-spacing: 0.08em;
    color: var(--wine);
    text-transform: uppercase;
  }

  .back-panel {
    position: absolute;
    left: -10px;
    top: 50%;
    width: 600px;
    height: 600px;
    margin-left: -300px;
    margin-top: -300px;
    border-radius: 50%;
    background: var(--wine);
  }
  .back-brand {
    position: absolute;
    left: 0;
    top: 0;
    width: 270px;
    height: 297px;
    display: flex;
    align-items: center;
    justify-content: center;
    gap: 10px;
    font-family: "Playfair Display", Georgia, serif;
    font-weight: 400;
    font-size: 19px;
    letter-spacing: 0.06em;
    color: var(--white);
    text-transform: uppercase;
  }
  .back-brand .dot {
    width: 12px;
    height: 12px;
    border: 1px solid var(--white);
    border-radius: 50%;
    flex: none;
  }

  .contact {
    position: absolute;
    left: 300px;
    top: 70px;
    right: 14px;
  }
  .contact__name {
    margin: 0;
    font-family: "Playfair Display", Georgia, serif;
    font-weight: 700;
    font-size: 21px;
    color: var(--navy);
    line-height: 1.1;
  }
  .contact__role {
    margin: 2px 0 18px;
    font-family: "Playfair Display", Georgia, serif;
    font-weight: 400;
    font-size: 15px;
    color: var(--wine);
  }
  .contact__list {
    list-style: none;
    margin: 0;
    padding: 0;
  }
  .contact__item {
    display: flex;
    align-items: center;
    gap: 10px;
    margin-bottom: 15px;
    font-family: "Libre Baskerville", Georgia, serif;
    font-size: 10px;
    color: var(--navy);
  }
  .contact__icon {
    width: 18px;
    height: 18px;
    flex: none;
  }
</style>
</head>
<body>
<main class="canvas">

  <section class="card card--front" aria-label="Card front">
    <div class="front-wordmark">Calm Brief Counsel</div>
  </section>

  <section class="card card--back" aria-label="Card back">
    <div class="back-panel"></div>
    <div class="back-brand"><span class="dot"></span>Calm Brief Counsel</div>

    <div class="contact">
      <h1 class="contact__name">Marissa Pendrell</h1>
      <p class="contact__role">Life Coach</p>
      <ul class="contact__list">
        <li class="contact__item">
          <svg class="contact__icon" viewBox="0 0 18 18" aria-hidden="true">
            <circle cx="9" cy="9" r="9" fill="var(--navy)"/>
            <rect x="4.5" y="5.8" width="9" height="6.4" fill="none" stroke="var(--white)" stroke-width="1"/>
            <path d="M4.5 5.8 L9 9.6 L13.5 5.8" fill="none" stroke="var(--white)" stroke-width="1"/>
          </svg>
          marissa@calmbriefcounsel.net
        </li>
        <li class="contact__item">
          <svg class="contact__icon" viewBox="0 0 18 18" aria-hidden="true">
            <circle cx="9" cy="9" r="9" fill="var(--navy)"/>
            <circle cx="9" cy="9" r="5" fill="none" stroke="var(--white)" stroke-width="1"/>
            <ellipse cx="9" cy="9" rx="2.2" ry="5" fill="none" stroke="var(--white)" stroke-width="1"/>
            <line x1="4" y1="9" x2="14" y2="9" stroke="var(--white)" stroke-width="1"/>
          </svg>
          calmbriefcounsel.net
        </li>
        <li class="contact__item">
          <svg class="contact__icon" viewBox="0 0 18 18" aria-hidden="true">
            <circle cx="9" cy="9" r="9" fill="var(--navy)"/>
          </svg>
          @calmbriefcounsel
        </li>
      </ul>
    </div>
  </section>

</main>
</body>
</html>
```